New website

Our website (www.larchvale.com) needs to be replaced with something gorgeous and glossy. We do like the text of our current website but have many new images to put on the site. We want to create a website that shows viewers what our team can do, and how we can create something amazing for them and their homes.

Coding

```html
<!DOCTYPE html>
<html lang="en">
<head>
<meta charset="utf-8">
<title>Larchvale Landscaping</title>
<link href="https://fonts.googleapis.com/css2?family=Tinos:wght@400&family=Nunito+Sans:ital,wght@0,400;0,600;0,700;1,400&display=swap" rel="stylesheet">
<style>
:root{
  --green:#1ba354;
  --blue:#2b7fc9;
  --ink:#2b2b2b;
  --body:#555;
  --dark:#3c3c3c;
  --leaf:#dcefc9;
  --white:#fff;
}
*{box-sizing:border-box;margin:0;padding:0}
html,body{width:1200px;height:3978px;overflow:hidden;background:var(--white)}
body{font-family:"Nunito Sans",sans-serif;color:var(--body);position:relative}
.page{position:relative;width:1200px;height:3978px;overflow:hidden}
.abs{position:absolute}
.serif{font-family:"Tinos",serif;font-weight:400;color:var(--ink);text-transform:uppercase}
.btn{position:absolute;background:var(--green);color:var(--white);font-weight:700;font-size:12px;border-radius:30px;display:flex;align-items:center;justify-content:center;text-transform:uppercase;letter-spacing:.2px}
.copy p{font-size:13px;line-height:22.4px}
.copy p+p{margin-top:14px}
.leaf-area{position:absolute;background:linear-gradient(180deg,rgba(220,239,201,0),var(--leaf) 30%,var(--leaf) 70%,rgba(220,239,201,0))}

/* hero */
.hero{position:absolute;left:0;top:0;width:1200px;height:680px}
.hero-photo{position:absolute;inset:0;background:linear-gradient(100deg,#3c5a22 0%,#5b7a2a 35%,#8a7c3a 60%,#b7a140 80%,#6a8a2e 100%)}
.logo{position:absolute;left:90px;top:26px;color:var(--white);font-family:"Tinos",serif;font-size:28px;letter-spacing:6px}
.logo small{display:block;font-family:"Nunito Sans",sans-serif;font-size:8px;letter-spacing:9px;text-align:center;margin-top:-2px}
.nav{position:absolute;left:483px;top:33px;display:flex;gap:25px;color:var(--white);font-size:12px;font-weight:600}
.hero-rule{position:absolute;left:90px;right:90px;top:82px;height:1px;background:rgba(255,255,255,.35)}
.hero h1{position:absolute;left:90px;top:180px;color:var(--white);font-size:63px;line-height:63px}
.hero .tag{position:absolute;left:90px;top:384px;color:var(--white);font-size:14px;font-weight:600}
.scroll{position:absolute;left:578px;top:570px;width:44px;height:68px;border:2px solid var(--white);border-radius:22px}

/* about */
.photo-circle{position:absolute;border-radius:50%;border:5px solid var(--blue)}
.about h2{position:absolute;left:571px;top:776px;font-size:38px}
.about .sub{position:absolute;left:571px;top:823px;color:var(--blue);font-size:16px}

/* services */
.services-bg{position:absolute;left:0;top:1160px;width:1200px;height:800px;background:radial-gradient(ellipse at 50% 40%,#fff 25%,#e9e9e9 75%,#fff 100%);clip-path:ellipse(110% 50% at 50% 50%)}
.services h2{position:absolute;left:0;width:1200px;text-align:center;top:1237px;font-size:38px}
.pill{position:absolute;left:438px;top:1315px;width:323px;height:491px;border-radius:162px;background:#e6e6e6}
.plant-area{position:absolute;left:488px;top:1360px;width:223px;height:400px;border-radius:24px;background:linear-gradient(180deg,#cfe6b4 0%,#9fcd6a 55%,#7a6a55 88%,#5a4636 100%)}
.svc{position:absolute;font-size:20px;line-height:27px}
.svc.left{text-align:right;width:260px;left:59px}
.svc.right{left:882px;width:260px}
.ico{position:absolute;width:72px;height:72px;border-radius:50%;display:flex;align-items:center;justify-content:center}

/* why */
.why h2{position:absolute;left:119px;top:1995px;font-size:38px}

/* testimonial */
.testi-bg{position:absolute;left:0;top:2420px;width:1200px;height:510px;background:linear-gradient(#fff 0%,#fff 55%,#ececec 100%);border-radius:0 0 50% 50%/0 0 28% 28%}
.testi h2{position:absolute;left:0;width:1200px;text-align:center;top:2497px;font-size:38px}
.dots{position:absolute;display:flex;gap:6px}
.dots i{display:block;width:22px;height:5px;border-radius:3px;background:var(--green)}
.dots i.on{background:var(--blue)}

/* footer */
.footer-bg{position:absolute;left:0;top:3390px;width:1200px;height:588px}
.foot h3{position:absolute;font-family:"Tinos",serif;font-weight:400;color:var(--white);font-size:19px;text-transform:uppercase}
.foot ul{list-style:none;position:absolute;color:#ddd;font-size:12.5px;line-height:31px}
.foot .txt{position:absolute;color:#ddd;font-size:13px;line-height:22px}
</style>
</head>
<body>
<div class="page">

<section class="hero">
  <div class="hero-photo" role="img" aria-label="Gardener in orange cap kneeling among flowering shrubs with a bucket"></div>
  <div class="logo">LARCHVALE<small>LANDSCAPING</small></div>
  <nav class="nav"><span>HOME</span><span>ABOUT US</span><span>OUR SERVICES</span><span>BLOG</span><span>CONTACT US</span></nav>
  <div class="btn" style="left:939px;top:20px;width:172px;height:42px">Make a Payment</div>
  <div class="hero-rule"></div>
  <h1 class="serif">Welcome to<br>experts for all<br>seasons</h1>
  <div class="tag">More Than Just Landscaping &amp; Snow Removal</div>
  <div class="btn" style="left:90px;top:429px;width:243px;height:48px">Schedule an Appointment</div>
  <div class="scroll"><svg width="40" height="64" viewBox="0 0 40 64"><path d="M20 22v20M14 36l6 6 6-6" stroke="#fff" stroke-width="2" fill="none"/></svg></div>
  <svg class="abs" style="left:0;top:560px" width="1200" height="120" viewBox="0 0 1200 120">
    <path d="M0 32 Q600 170 1200 22 L1200 120 L0 120Z" fill="#fff"/>
    <path d="M0 32 Q600 170 1200 22" stroke="var(--blue)" stroke-width="6" fill="none"/>
  </svg>
</section>

<section class="about">
  <div class="leaf-area" role="img" aria-label="Climbing vine with green leaves" style="left:0;top:610px;width:110px;height:280px"></div>
  <div class="photo-circle" role="img" aria-label="Gardener trimming a round shrub with shears" style="left:154px;top:750px;width:346px;height:346px;background:linear-gradient(135deg,#2f4d1f,#6b8c3a 60%,#3a5a24)"></div>
  <h2 class="serif">About Us</h2>
  <div class="sub">A Passionate Landscaping Company</div>
  <div class="copy abs" style="left:571px;top:862px;width:476px">
    <p>Established in 2005 as a way to pay for college tuition, Larchvale has instead become our passion. With a garage sale mower and a commitment to doing every job well, our list of satisfied customers grew quickly over the years.</p>
    <p>While the scope of our landscaping company has grown, our way of doing business has not. It is still rooted in the desire to do quality work whether the job includes a simple tree service or the installation of an entire irrigation system, provide exceptional value, and to serve our clients with integrity.</p>
  </div>
</section>

<section class="services">
  <div class="services-bg"></div>
  <h2 class="serif">Our Services</h2>
  <div class="pill"></div>
  <div class="plant-area" role="img" aria-label="Young green plant growing from a mound of soil"></div>

  <div class="svc left serif" style="top:1367px">Irrigation<br>Installation</div>
  <div class="svc left serif" style="top:1483px">Lawn<br>Maintenance</div>
  <div class="svc left serif" style="top:1600px">Landscape<br>Maintenance</div>
  <div class="svc left serif" style="top:1716px">Lawn<br>Core Aeration</div>
  <div class="svc right serif" style="top:1367px">Lawn<br>Fertilization</div>
  <div class="svc right serif" style="top:1483px">Mulch<br>Bark Installation</div>
  <div class="svc right serif" style="top:1600px">Snow<br>Plowing</div>
  <div class="svc right serif" style="top:1716px">Tree Services &amp;<br>Shrub Pruning</div>

  <div class="ico" style="left:342px;top:1358px;background:var(--blue)"><svg width="34" height="34" viewBox="0 0 34 34" fill="none" stroke="#fff" stroke-width="2"><path d="M17 4c-5 8-8 12-8 17a8 8 0 0 0 16 0c0-5-3-9-8-17z"/></svg></div>
  <div class="ico" style="left:342px;top:1474px;background:var(--green)"><svg width="34" height="34" viewBox="0 0 34 34" fill="none" stroke="#fff" stroke-width="2"><path d="M4 8l8 10h16v8H8l-2-8"/><circle cx="11" cy="27" r="3"/><circle cx="25" cy="27" r="3"/></svg></div>
  <div class="ico" style="left:342px;top:1590px;background:var(--green)"><svg width="34" height="34" viewBox="0 0 34 34" fill="none" stroke="#fff" stroke-width="2"><circle cx="11" cy="11" r="6"/><path d="M11 17v13M4 30h26"/><circle cx="24" cy="14" r="5"/><path d="M24 19v11"/></svg></div>
  <div class="ico" style="left:342px;top:1706px;background:var(--green)"><svg width="34" height="34" viewBox="0 0 34 34" fill="none" stroke="#fff" stroke-width="2"><path d="M20 4v18M14 22h12l-2 6H16zM6 30h22"/></svg></div>
  <div class="ico" style="left:782px;top:1358px;background:var(--green)"><svg width="34" height="34" viewBox="0 0 34 34" fill="none" stroke="#fff" stroke-width="2"><path d="M6 26h22M10 26c0-8 4-14 12-16-1 8-5 14-12 16z"/></svg></div>
  <div class="ico" style="left:782px;top:1474px;background:var(--green)"><svg width="34" height="34" viewBox="0 0 34 34" fill="none" stroke="#fff" stroke-width="2"><path d="M17 30V12M17 16c-4 0-7-3-7-7 4 0 7 3 7 7zM17 16c4 0 7-3 7-7-4 0-7 3-7 7zM8 30h18"/></svg></div>
  <div class="ico" style="left:782px;top:1590px;background:var(--green)"><svg width="34" height="34" viewBox="0 0 34 34" fill="none" stroke="#fff" stroke-width="2"><rect x="4" y="10" width="16" height="12"/><path d="M20 14h6l4 5v3H20"/><circle cx="9" cy="25" r="3"/><circle cx="24" cy="25" r="3"/></svg></div>
  <div class="ico" style="left:782px;top:1706px;background:var(--green)"><svg width="34" height="34" viewBox="0 0 34 34" fill="none" stroke="#fff" stroke-width="2"><circle cx="9" cy="25" r="4"/><circle cx="25" cy="25" r="4"/><path d="M12 22L26 4M22 22L8 4"/></svg></div>

  <div class="btn" style="left:500px;top:1843px;width:200px;height:48px">View More Services</div>
</section>

<section class="why">
  <div class="leaf-area" role="img" aria-label="Climbing vine with green leaves" style="left:1080px;top:1870px;width:120px;height:240px"></div>
  <h2 class="serif">Why Choose Us ?</h2>
  <div class="copy abs" style="left:119px;top:2052px;width:474px">
    <p>You shouldn't have to spend hours on grounds maintenance to enjoy a well-designed and well-maintained yard. The landscaping professionals at Larchvale can handle your landscape maintenance, so you can focus on the demands of your family, job, and more.</p>
    <p>We're top rated landscapers; our passion for the work we do is what makes us a clear leader among other landscaping companies in the area. When you are a part of our Lawn Maintenance program, we provide regularly-scheduled maintenance visits. Whether it is lawn mowing, trimming and edging, lawn fertilization and weed control, tree care, shrub pruning, landscape bed maintenance, monitoring your irrigation system, or designing and installing seasonal color displays, Larchvale handles everything so you don't have to.</p>
  </div>
  <div class="btn" style="left:119px;top:2354px;width:155px;height:48px">Contact Us</div>
  <div class="photo-circle" role="img" aria-label="Older gardener trimming a tall hedge with an electric trimmer" style="left:667px;top:1971px;width:442px;height:442px;border-color:transparent var(--blue) var(--blue) transparent;background:linear-gradient(135deg,#1f3d18,#3e6a28 55%,#86a25a)"></div>
</section>

<section class="testi">
  <div class="testi-bg"></div>
  <h2 class="serif">What People Says</h2>
  <div class="abs" style="left:0;width:1200px;top:2548px;text-align:center;font-size:15px;line-height:23px">After Trying Four Different Companies Over the Last Four Years,<br>I Finally Found Larchvale!</div>
  <div class="abs" style="left:560px;top:2604px;width:80px;height:80px;border-radius:50%;background:var(--blue)"><svg width="80" height="80" viewBox="0 0 80 80" fill="#fff"><circle cx="30" cy="44" r="10"/><path d="M20 44c0-12 6-18 14-20l1 4c-6 2-8 7-8 12z"/><circle cx="52" cy="44" r="10"/><path d="M42 44c0-12 6-18 14-20l1 4c-6 2-8 7-8 12z"/></svg></div>
  <div class="abs" style="left:250px;width:700px;top:2701px;text-align:center;font-style:italic;font-size:16px;line-height:27px">"Other companies couldn't effectively snowplow our long and twisted driveway. After trying four different companies over the last four years, I finally found Larchvale — and I won't be using any other company from now on. You are timely, dependable and most important, you do a great job!"</div>
  <div class="abs serif" style="left:0;width:1200px;text-align:center;top:2816px;font-size:17px">Jane, Elm</div>
  <div class="dots" style="left:561px;top:2856px"><i></i><i class="on"></i><i></i></div>
</section>

<section class="gallery">
  <div class="leaf-area" role="img" aria-label="Climbing vine with green leaves" style="left:0;top:2860px;width:110px;height:320px"></div>
  <h2 class="abs serif" style="left:0;width:1200px;text-align:center;top:2977px;font-size:38px">Our Gallery</h2>
  <div class="abs" role="img" aria-label="Gardener in red shirt kneeling in a flower bed" style="left:94px;top:3064px;width:192px;height:192px;border-radius:50%;background:linear-gradient(135deg,#3f6a22,#a0b040 60%,#c3472a)"></div>
  <div class="abs" role="img" aria-label="Wooden boardwalk through a wooded garden" style="left:290px;top:3064px;width:192px;height:192px;border-radius:50%;background:linear-gradient(135deg,#2d4a20,#5d7c38 55%,#7a6a50)"></div>
  <div class="abs" role="img" aria-label="Modern house with landscaped front lawn" style="left:486px;top:3047px;width:226px;height:226px;border-radius:50%;background:linear-gradient(160deg,#c9d3dc,#8c96a0 45%,#4d7a34)"></div>
  <div class="abs" style="left:575px;top:3136px;width:48px;height:48px;border-radius:50%;background:rgba(43,127,201,.85)"><svg width="48" height="48" viewBox="0 0 48 48" fill="none" stroke="#fff" stroke-width="2.5"><path d="M21 27l6-6M18 24l-3 3a4 4 0 0 0 6 6l3-3M30 24l3-3a4 4 0 0 0-6-6l-3 3"/></svg></div>
  <div class="abs" role="img" aria-label="Trimmed hedges around a garden pond" style="left:716px;top:3064px;width:192px;height:192px;border-radius:50%;background:linear-gradient(160deg,#6b8f3a,#4e7a2c 60%,#8aa05c)"></div>
  <div class="abs" role="img" aria-label="Gardener planting among red foliage" style="left:912px;top:3064px;width:192px;height:192px;border-radius:50%;background:linear-gradient(160deg,#507a2c,#8a3a3a 60%,#6a4a2a)"></div>
  <div class="dots" style="left:561px;top:3297px"><i></i><i class="on"></i><i></i></div>
</section>

<footer class="foot">
  <svg class="footer-bg" width="1200" height="588" viewBox="0 0 1200 588">
    <path d="M0 92 Q600 -40 1200 92 L1200 588 L0 588Z" fill="var(--dark)"/>
    <path d="M0 92 Q600 -40 1200 92" stroke="var(--blue)" stroke-width="8" fill="none"/>
  </svg>
  <h2 class="abs serif" style="left:90px;top:3508px;font-size:36px;color:#fff">Contact Us Today</h2>
  <div class="txt" style="left:90px;top:3555px;width:530px;font-size:13px">We're top rated landscapers; our passion for the work we do is what makes us a clear leader among other landscaping companies in the area.</div>
  <div class="btn" style="left:956px;top:3539px;width:154px;height:48px">Get Started</div>
  <div class="abs" style="left:90px;top:3628px;width:1020px;height:1px;background:#5a5a5a"></div>

  <div class="logo" style="left:90px;top:3758px;font-size:30px">LARCHVALE<small>LANDSCAPING</small></div>

  <h3 style="left:401px;top:3678px">Our Gallery</h3>
  <ul style="left:401px;top:3705px"><li>Home</li><li>About Us</li><li>Our Services</li><li>Testimonials</li><li>Contact Us</li></ul>

  <h3 style="left:619px;top:3678px">Working Hours</h3>
  <svg class="abs" style="left:619px;top:3710px" width="16" height="16" viewBox="0 0 16 16"><circle cx="8" cy="8" r="7" fill="var(--green)"/><path d="M8 4v4l3 2" stroke="#fff" stroke-width="1.5" fill="none"/></svg>
  <div class="txt" style="left:643px;top:3706px">Monday-Saturday:<br>7:00am-7:00pm</div>
  <h3 style="left:619px;top:3775px;font-size:17px">Contact Us</h3>
  <svg class="abs" style="left:619px;top:3805px" width="16" height="16" viewBox="0 0 16 16"><path d="M3 2h3l1 3-2 1a8 8 0 0 0 5 5l1-2 3 1v3a1 1 0 0 1-1 1A12 12 0 0 1 2 3a1 1 0 0 1 1-1z" fill="var(--green)"/></svg>
  <div class="txt" style="left:643px;top:3800px">Call us:<br><span style="font-size:15px">(555) 214-7730</span></div>

  <h3 style="left:870px;top:3678px">Newsleter</h3>
  <div class="txt" style="left:870px;top:3706px;font-size:12px">Subscribe to our newsletter</div>
  <div class="abs" style="left:870px;top:3740px;width:240px;height:38px;border-radius:20px;background:#525252;color:#eee;font-size:12px;padding:11px 20px">Email Address</div>
  <svg class="abs" style="left:1075px;top:3750px" width="18" height="18" viewBox="0 0 18 18"><path d="M2 9l14-7-5 14-2-6z" fill="var(--green)"/></svg>
  <div class="abs" style="left:870px;top:3808px;display:flex;gap:20px">
    <i style="display:block;width:14px;height:14px;border-radius:50%;background:#fff"></i>
    <i style="display:block;width:14px;height:14px;border-radius:50%;background:#fff"></i>
    <i style="display:block;width:14px;height:14px;border-radius:50%;background:#fff"></i>
    <i style="display:block;width:14px;height:14px;border-radius:50%;background:#fff"></i>
  </div>

  <div class="abs" style="left:90px;top:3917px;width:1020px;height:1px;background:#5a5a5a"></div>
  <div class="abs" style="left:0;width:1200px;top:3936px;text-align:center;color:#fff;font-size:13px">©2025 Larchvale Landscaping - All rights reserved.</div>
  <div class="abs" style="left:1130px;top:3904px;width:50px;height:50px;border-radius:50%;background:var(--green)"><svg width="50" height="50" viewBox="0 0 50 50"><path d="M20 28l5-5 5 5" stroke="#fff" stroke-width="2" fill="none"/></svg></div>
</footer>

</div>
</body>
</html>
```